Website design for new health & wellness company

We need our website to be designed in a user friendly way. Needs to be aesthetically pleasing to viewer and easy to navigate and upload content for our small team . The logo should be completely redesigned , please do not reference the current one thats on our site for a starting place. (included below though) We want to move away from that.

the website is : www.brightpathmoments.net

We are a small group of writers/coaches who believe that to change the world you have to be the change and we provide tips/suggestions for every day life that if followed can make a huge difference in your life and overall being.

Target Market(s)

Men and women ages 22 to 50

Industry/Entity Type

Health And Wellness

Logo Text

Cultivate the life of your dreams

Coding

Coded - Design and coding required

Number of Pages Required

3 page

Font styles to use
Sans Serif

Colors

Designer to choose colors to be used in the design.

Requirements
Must have
• Easy to navigate. Mobile friendly. Gender neutral, should appeal to both.

```html
<!DOCTYPE html>
<html lang="en">
<head>
<meta charset="utf-8">
<title>Bright Path Moments – Health &amp; Wellness</title>
<link href="https://fonts.googleapis.com/css2?family=Lato:wght@400;700;900&display=swap" rel="stylesheet">
<style>
:root{
  --brand:#2c5878;
  --brand-dark:#1f4562;
  --ink:#222;
  --muted:#666;
  --line:#d9dcdf;
  --footer:#eeeff2;
  --white:#fff;
}
*{box-sizing:border-box;margin:0;padding:0}
html,body{width:1200px;height:3607px;overflow:hidden}
body{position:relative;background:var(--white);font-family:"Lato",Arial,sans-serif;color:var(--ink)}
.photo{position:absolute;display:block}

/* header */
.site-header{position:absolute;left:0;top:0;width:1200px;height:82px;background:var(--white)}
.brand{position:absolute;left:132px;top:18px;display:flex;align-items:center;gap:10px}
.brand-dot{width:34px;height:34px;border-radius:50%;background:var(--brand);flex:none}
.brand-name{display:block;font-size:18px;font-weight:900;line-height:20px;color:var(--brand);letter-spacing:.5px;white-space:nowrap}
.main-nav{position:absolute;left:404px;top:30px;display:flex}
.main-nav a{display:block;height:26px;line-height:26px;padding:0 12px;margin-right:26px;font-size:11px;font-weight:700;color:var(--ink);text-decoration:none;text-transform:uppercase}
.main-nav a.active{background:var(--brand);color:var(--white)}
.search{position:absolute;left:928px;top:24px;width:140px;height:36px;border:1px solid #ccc;font-size:10px;font-weight:700;padding:0 12px;line-height:34px;color:#444}
.search svg{position:absolute;right:10px;top:11px}

/* hero */
.hero{position:absolute;left:0;top:82px;width:1200px;height:389px;background:linear-gradient(100deg,#c9d7c7 0%,#a9b98e 35%,#8fa35e 60%,#6f8747 100%)}
.hero h1{position:absolute;left:209px;top:132px;font-size:44px;font-weight:700;color:var(--white)}
.hero p{position:absolute;left:209px;top:192px;font-size:17px;font-weight:700;color:var(--white)}
.dots{position:absolute;left:548px;top:328px;display:flex;gap:14px}
.dots span{width:10px;height:10px;border-radius:50%;background:var(--white)}
.dots span.on{background:transparent;border:2px solid var(--white)}

/* tags */
.tag{position:absolute;height:44px;line-height:44px;padding:0 18px;background:var(--brand);color:var(--white);font-size:14px;font-weight:700;text-transform:uppercase}

.meta{font-size:10px;color:#333}
.meta svg{vertical-align:-1px;margin:0 3px 0 6px}
.small-title{font-size:12px;font-weight:700;line-height:18px;color:var(--ink)}

/* latest news */
.news-lead{position:absolute;left:132px;top:594px;width:412px;height:435px;border:1px solid var(--line)}
.news-lead .body{position:absolute;left:26px;top:300px;width:360px}
.news-lead h3{font-size:15px;font-weight:700;margin:10px 0 12px}
.news-lead p{font-size:12px;line-height:20px;color:var(--muted)}
.side-item{position:absolute;left:560px;width:240px;height:72px}
.side-item .thumb{position:absolute;left:0;top:0;width:82px;height:72px}
.side-item .txt{position:absolute;left:97px;top:0;width:100px}
.post-item{position:absolute;width:290px;height:67px}
.post-item .thumb{position:absolute;left:0;top:0;width:115px;height:67px}
.post-item .txt{position:absolute;left:130px;top:12px}

/* grids */
.grid-card{position:absolute;width:300px}
.grid-card .img{height:240px}
.grid-card .meta{margin-top:24px}
.grid-card h3{margin-top:12px;width:240px;font-size:18px;font-weight:400;line-height:26px;text-transform:uppercase;color:#111}

/* brain */
.brain-card{position:absolute;left:132px;width:614px;height:154px;border:1px solid var(--line)}
.brain-card .img{position:absolute;left:12px;top:12px;width:178px;height:128px}
.brain-card .txt{position:absolute;left:232px;top:24px;width:330px}
.brain-card h3{font-size:15px;font-weight:700;margin:14px 0 14px}
.brain-card p{font-size:12px;line-height:20px;color:var(--muted)}

/* featured */
.feat-card{position:absolute;top:2698px;width:221px;height:325px;border:1px solid var(--line)}
.feat-card .img{height:159px}
.feat-card .txt{padding:20px 16px 0}
.feat-card h3{font-size:15px;font-weight:400;line-height:22px;margin:10px 0 12px;color:#111}
.feat-card p{font-size:12px;line-height:18px;color:#444}
.arrows{position:absolute;left:1022px;top:2640px;display:flex;gap:14px}

/* footer */
.site-footer{position:absolute;left:0;top:3086px;width:1200px;height:521px;background:var(--footer)}
.site-footer .brand{left:103px;top:64px}
.follow{position:absolute;left:190px;top:190px;font-size:11px;font-weight:700;color:var(--brand);text-transform:uppercase}
.social{position:absolute;left:137px;display:flex;align-items:center;gap:14px;font-size:12px;color:#333}
.social span.ic{width:24px;height:24px;border-radius:50%;background:var(--brand)}
.f-head{position:absolute;top:74px;font-size:14px;font-weight:700;color:var(--brand);text-transform:uppercase}
.f-post{position:absolute;left:394px;width:300px;height:53px}
.f-post .thumb{position:absolute;left:0;top:0;width:106px;height:53px}
.f-post .txt{position:absolute;left:128px;top:4px}
.f-post h4{font-size:13px;font-weight:700;color:#111}
.f-post p{font-size:11px;color:#555;margin-top:6px}
.about{position:absolute;left:770px;top:118px;width:298px;font-size:12px;line-height:19px;color:#555;text-align:justify}
.about p+p{margin-top:20px}
.read-more{position:absolute;left:770px;top:348px;height:25px;line-height:25px;padding:0 8px;background:var(--brand-dark);color:var(--white);font-size:10px;font-weight:700;text-transform:uppercase}
.f-rule{position:absolute;left:132px;top:440px;width:936px;height:1px;background:#d8dadd}
.copyright{position:absolute;left:0;top:478px;width:1200px;text-align:center;font-size:10px;color:#666}
</style>
</head>
<body>

<header class="site-header">
  <div class="brand"><span class="brand-dot"></span><span class="brand-name">BRIGHT PATH<br>MOMENTS</span></div>
  <nav class="main-nav">
    <a class="active" href="#">Home</a><a href="#">Plate</a><a href="#">Brain</a><a href="#">Body</a><a href="#">Contact Us</a>
  </nav>
  <div class="search">SEARCH
    <svg width="12" height="12" viewBox="0 0 12 12"><circle cx="5" cy="5" r="3.8" fill="none" stroke="#333" stroke-width="1.5"/><line x1="8" y1="8" x2="11" y2="11" stroke="#333" stroke-width="1.5"/></svg>
  </div>
</header>

<section class="hero" role="img" aria-label="Runner on a sunny country path through grassy fields">
  <h1>Health &amp; Wellness</h1>
  <p>Lorem Ipsum is simply dummy text</p>
  <div class="dots"><span></span><span class="on"></span><span></span><span></span><span></span></div>
</section>

<div class="tag" style="left:132px;top:517px">Latest News</div>
<div class="tag" style="left:782px;top:517px">Latest Posts</div>

<article class="news-lead">
  <div class="photo" role="img" aria-label="Person with arms raised in beach grass by the sea" style="left:0;top:0;width:410px;height:277px;background:linear-gradient(180deg,#a9cbe6 0%,#d8e4ea 45%,#c9b48a 75%,#a99466 100%)"></div>
  <div class="body">
    <div class="meta">June 05, 2017 |<svg width="10" height="9" viewBox="0 0 10 9"><path d="M1 1h8v5H4L2 8V6H1z" fill="#333"/></svg>3 Comments</div>
    <h3>There are many variations of passages</h3>
    <p>There are many variations of passages of Loreen Ipsum available, but the majority have suffered alteration in some form, by injected humour, or randomise</p>
  </div>
</article>

<div class="side-item" style="top:594px"><div class="thumb photo" role="img" aria-label="Sunset silhouette" style="background:linear-gradient(135deg,#e3a84a,#7a4a22)"></div><div class="txt"><div class="meta">March 17, 2017</div><div class="small-title" style="margin-top:6px">Lorem Ipsum is simply dum</div></div></div>
<div class="side-item" style="top:685px"><div class="thumb photo" role="img" aria-label="Hands holding a red heart" style="background:linear-gradient(135deg,#3d5566,#b84a4a)"></div><div class="txt"><div class="meta">March 17, 2017</div><div class="small-title" style="margin-top:6px">Lorem Ipsum is simply dummy</div></div></div>
<div class="side-item" style="top:777px"><div class="thumb photo" role="img" aria-label="Family outdoors" style="background:linear-gradient(135deg,#9a8f84,#4d3f36)"></div><div class="txt"><div class="meta">March 17, 2017</div><div class="small-title" style="margin-top:6px">Lorem Ipsum is simply dummy</div></div></div>
<div class="side-item" style="top:868px"><div class="thumb photo" role="img" aria-label="Person stretching on grass" style="background:linear-gradient(135deg,#a7c98a,#5f8b57)"></div><div class="txt"><div class="meta">March 17, 2017</div><div class="small-title" style="margin-top:6px">Lorem Ipsum is simply dummy</div></div></div>
<div class="side-item" style="top:957px"><div class="thumb photo" role="img" aria-label="Couple relaxing" style="background:linear-gradient(135deg,#c7b4a0,#6b5646)"></div><div class="txt"><div class="meta">March 17, 2017</div><div class="small-title" style="margin-top:6px">Lorem Ipsum is simply dummy</div></div></div>

<div class="post-item" style="left:784px;top:589px"><div class="thumb photo" role="img" aria-label="Sunset over a field" style="background:linear-gradient(180deg,#f2b64a,#8d6a2e)"></div><div class="txt"><div class="meta">June 06, 2017</div><div class="small-title" style="margin-top:6px">Lorem Ipsum is simply dum</div></div></div>
<div class="post-item" style="left:784px;top:678px"><div class="thumb photo" role="img" aria-label="Hands holding a red heart" style="background:linear-gradient(135deg,#e8e8ea,#c9484d)"></div><div class="txt"><div class="meta">June 06, 2017</div><div class="small-title" style="margin-top:6px">Lorem Ipsum is simply dum</div></div></div>
<div class="post-item" style="left:784px;top:770px"><div class="thumb photo" role="img" aria-label="Paper family cut-outs" style="background:linear-gradient(135deg,#f1e4dc,#c23b3b)"></div><div class="txt"><div class="meta">June 06, 2017</div><div class="small-title" style="margin-top:6px">Lorem Ipsum is simply dum</div></div></div>
<div class="post-item" style="left:784px;top:861px"><div class="thumb photo" role="img" aria-label="Portrait in low light" style="background:linear-gradient(135deg,#8a8f96,#33383e)"></div><div class="txt"><div class="meta">June 06, 2017</div><div class="small-title" style="margin-top:6px">Lorem Ipsum is simply dum</div></div></div>
<div class="post-item" style="left:784px;top:952px"><div class="thumb photo" role="img" aria-label="Child jumping on green grass" style="background:linear-gradient(180deg,#d4dc6a,#4f9a3c)"></div><div class="txt"><div class="meta">June 06, 2017</div><div class="small-title" style="margin-top:6px">Lorem Ipsum is simply dum</div></div></div>

<div class="tag" style="left:132px;top:1080px">Plate</div>
<article class="grid-card" style="left:132px;top:1157px"><div class="img" role="img" aria-label="Festive plate with vegetables on yellow table" style="background:linear-gradient(135deg,#f1c53a,#c7b9a6 50%,#d94c3a)"></div><div class="meta">June 05, 2017 |<svg width="10" height="9" viewBox="0 0 10 9"><path d="M1 1h8v5H4L2 8V6H1z" fill="#333"/></svg>3 Comments</div><h3>There are many variati ons of passages</h3></article>
<article class="grid-card" style="left:450px;top:1157px"><div class="img" role="img" aria-label="Flat bread and blossoms on a blue table" style="background:linear-gradient(135deg,#b9ccd8,#e7e2d8 50%,#a9c1cf)"></div><div class="meta">June 05, 2017 |<svg width="10" height="9" viewBox="0 0 10 9"><path d="M1 1h8v5H4L2 8V6H1z" fill="#333"/></svg>3 Comments</div><h3>There are many variati ons of passages</h3></article>
<article class="grid-card" style="left:770px;top:1157px"><div class="img" role="img" aria-label="Colourful ceramic plates seen from above" style="background:linear-gradient(135deg,#e6d8c4,#58a9a4 45%,#b1486a)"></div><div class="meta">June 05, 2017 |<svg width="10" height="9" viewBox="0 0 10 9"><path d="M1 1h8v5H4L2 8V6H1z" fill="#333"/></svg>3 Comments</div><h3>There are many variati ons of passages</h3></article>

<div class="tag" style="left:132px;top:1534px">Body</div>
<article class="grid-card" style="left:132px;top:1607px"><div class="img" role="img" aria-label="Waist measured with a tape on teal background" style="background:linear-gradient(135deg,#3aa2b2,#c9b9a4 55%,#2c8d9c)"></div><div class="meta">June 05, 2017 |<svg width="10" height="9" viewBox="0 0 10 9"><path d="M1 1h8v5H4L2 8V6H1z" fill="#333"/></svg>3 Comments</div><h3>There are many variati ons of passages</h3></article>
<article class="grid-card" style="left:450px;top:1607px"><div class="img" role="img" aria-label="Hands on a stomach" style="background:linear-gradient(135deg,#f2f0ec,#d6b8a2 60%,#c9a48b)"></div><div class="meta">June 05, 2017 |<svg width="10" height="9" viewBox="0 0 10 9"><path d="M1 1h8v5H4L2 8V6H1z" fill="#333"/></svg>3 Comments</div><h3>There are many variati ons of passages</h3></article>
<article class="grid-card" style="left:770px;top:1607px"><div class="img" role="img" aria-label="Smiling woman after a workout in a park" style="background:linear-gradient(135deg,#5e7a3e,#a7b98a 50%,#3f5a2e)"></div><div class="meta">June 05, 2017 |<svg width="10" height="9" viewBox="0 0 10 9"><path d="M1 1h8v5H4L2 8V6H1z" fill="#333"/></svg>3 Comments</div><h3>There are many variati ons of passages</h3></article>

<div class="tag" style="left:132px;top:2011px">Brain</div>
<div class="tag" style="left:774px;top:2011px">Recent</div>
<div class="tag" style="left:880px;top:2011px">Popular</div>

<article class="brain-card" style="top:2083px"><div class="img" role="img" aria-label="Glowing brain graphic on dark background" style="background:linear-gradient(135deg,#0c1a2a,#4c6f90 55%,#0b1522)"></div><div class="txt"><div class="meta">June 05, 2017 |<svg width="10" height="9" viewBox="0 0 10 9"><path d="M1 1h8v5H4L2 8V6H1z" fill="#333"/></svg>3 Comments</div><h3>It is a long established fact that a reader</h3><p>There are many variations of passages of Lorem Ipsum available, but the majority have suffered.</p></div></article>
<article class="brain-card" style="top:2254px"><div class="img" role="img" aria-label="Blue neural brain illustration" style="background:linear-gradient(135deg,#06234a,#2d8fd6 55%,#062044)"></div><div class="txt"><div class="meta">June 05, 2017 |<svg width="10" height="9" viewBox="0 0 10 9"><path d="M1 1h8v5H4L2 8V6H1z" fill="#333"/></svg>3 Comments</div><h3>It is a long established fact that a reader</h3><p>There are many variations of passages of Lorem Ipsum available, but the majority have suffered.</p></div></article>
<article class="brain-card" style="top:2424px"><div class="img" role="img" aria-label="Person in a suit holding a glowing brain" style="background:linear-gradient(135deg,#c9c6c2,#8a6a44 50%,#2a2b30)"></div><div class="txt"><div class="meta">June 05, 2017 |<svg width="10" height="9" viewBox="0 0 10 9"><path d="M1 1h8v5H4L2 8V6H1z" fill="#333"/></svg>3 Comments</div><h3>It is a long established fact that a reader</h3><p>There are many variations of passages of Lorem Ipsum available, but the majority have suffered.</p></div></article>

<div class="post-item" style="left:777px;top:2083px"><div class="thumb photo" role="img" aria-label="Sunset over a field" style="background:linear-gradient(180deg,#f2b64a,#8d6a2e)"></div><div class="txt"><div class="meta">June 06, 2017</div><div class="small-title" style="margin-top:6px">Lorem Ipsum is simply dum</div></div></div>
<div class="post-item" style="left:777px;top:2174px"><div class="thumb photo" role="img" aria-label="Hands holding a red heart" style="background:linear-gradient(135deg,#e8e8ea,#c9484d)"></div><div class="txt"><div class="meta">June 06, 2017</div><div class="small-title" style="margin-top:6px">Lorem Ipsum is simply dum</div></div></div>
<div class="post-item" style="left:777px;top:2266px"><div class="thumb photo" role="img" aria-label="Paper family cut-outs" style="background:linear-gradient(135deg,#f1e4dc,#c23b3b)"></div><div class="txt"><div class="meta">June 06, 2017</div><div class="small-title" style="margin-top:6px">Lorem Ipsum is simply dum</div></div></div>
<div class="post-item" style="left:777px;top:2357px"><div class="thumb photo" role="img" aria-label="Portrait in low light" style="background:linear-gradient(135deg,#8a8f96,#33383e)"></div><div class="txt"><div class="meta">June 06, 2017</div><div class="small-title" style="margin-top:6px">Lorem Ipsum is simply dum</div></div></div>
<div class="post-item" style="left:777px;top:2451px"><div class="thumb photo" role="img" aria-label="Child jumping on green grass" style="background:linear-gradient(180deg,#d4dc6a,#4f9a3c)"></div><div class="txt"><div class="meta">June 06, 2017</div><div class="small-title" style="margin-top:6px">Lorem Ipsum is simply dum</div></div></div>

<div class="tag" style="left:132px;top:2633px">Featured Posts</div>
<div class="arrows">
  <svg width="14" height="22" viewBox="0 0 14 22"><path d="M11 2L3 11l8 9" fill="none" stroke="#999" stroke-width="2"/></svg>
  <svg width="14" height="22" viewBox="0 0 14 22"><path d="M3 2l8 9-8 9" fill="none" stroke="#999" stroke-width="2"/></svg>
</div>
<article class="feat-card" style="left:132px"><div class="img" role="img" aria-label="Red heart with a stethoscope" style="background:linear-gradient(135deg,#5a5f66,#d23c3c 50%,#2fa7b8)"></div><div class="txt"><div class="meta">June 05, 2017</div><h3>There are many variations of passages</h3><p>It uses a dictionary of over 200 Latin words, combined with a handful of model.</p></div></article>
<article class="feat-card" style="left:373px"><div class="img" role="img" aria-label="Hand giving a thumbs up" style="background:linear-gradient(135deg,#1f3a52,#c99a7c 55%,#2a4660)"></div><div class="txt"><div class="meta">June 05, 2017</div><h3>There are many variations of passages</h3><p>It uses a dictionary of over 200 Latin words, combined with a handful of model.</p></div></article>
<article class="feat-card" style="left:611px"><div class="img" role="img" aria-label="Person resting on a bed by a bright window" style="background:linear-gradient(135deg,#e9f1f6,#9fc1d8 55%,#5c87a8)"></div><div class="txt"><div class="meta">June 05, 2017</div><h3>There are many variations of passages</h3><p>It uses a dictionary of over 200 Latin words, combined with a handful of model.</p></div></article>
<article class="feat-card" style="left:849px"><div class="img" role="img" aria-label="Running shoes on a road at sunset" style="background:linear-gradient(135deg,#e8b47a,#b8463a 55%,#5d4a3e)"></div><div class="txt"><div class="meta">June 05, 2017</div><h3>There are many variations of passages</h3><p>It uses a dictionary of over 200 Latin words, combined with a handful of model.</p></div></article>

<footer class="site-footer">
  <div class="brand"><span class="brand-dot"></span><span class="brand-name">BRIGHT PATH<br>MOMENTS</span></div>
  <div class="follow">Follow us</div>
  <div class="social" style="top:238px"><span class="ic"></span>Like us on Circlebook</div>
  <div class="social" style="top:279px"><span class="ic"></span>Follow us on Chirpline</div>
  <div class="social" style="top:320px"><span class="ic"></span>Follow us on Plusroom</div>
  <div class="social" style="top:361px"><span class="ic"></span>Follow us on Linkwell</div>

  <div class="f-head" style="left:394px">Recent Posts</div>
  <div class="f-post" style="top:115px"><div class="thumb photo" role="img" aria-label="Healthy food bowls" style="background:linear-gradient(135deg,#b9c76a,#d0563e)"></div><div class="txt"><h4>There are many variations</h4><p>It uses a dictionary of over</p></div></div>
  <div class="f-post" style="top:187px"><div class="thumb photo" role="img" aria-label="Green leafy scene" style="background:linear-gradient(135deg,#9ccb5a,#3f7a34)"></div><div class="txt"><h4>It is a long established fact</h4><p>It uses a dictionary of over</p></div></div>
  <div class="f-post" style="top:257px"><div class="thumb photo" role="img" aria-label="Wooden table with food" style="background:linear-gradient(135deg,#d6a06a,#7c5032)"></div><div class="txt"><h4>Lorem Ipsum text</h4><p>It uses a dictionary of over</p></div></div>
  <div class="f-post" style="top:322px"><div class="thumb photo" role="img" aria-label="Hands holding a small plant" style="background:linear-gradient(135deg,#f0d48a,#8ab04e)"></div><div class="txt"><h4>Contrary to popular belie</h4><p>It uses a dictionary of over</p></div></div>

  <div class="f-head" style="left:770px">About Bright Path</div>
  <div class="about">
    <p>There are many variations of passages of Lorem Ipsum available, but the majority have suffered alteration in some form, by injected humour, or randomised words which don't look even slightly believable.</p>
    <p>It is a long established fact that a reader will be distracted by the readable content of a page when looking at its layout. The point of using Lorem Ipsum is that it has a more-or-less normal distribution of letters, as opposed.</p>
  </div>
  <div class="read-more">Read more</div>

  <div class="f-rule"></div>
  <div class="copyright">Copyrights @ 2017 All Rights Reserved</div>
</footer>

</body>
</html>
```